Redesign of my business card

I would like to redesign my business card attached is my old version the new one. I’d like using my new logo that you designed that looks amazing thank you.

I would like the new card to be minimalist Brook Estate Group’s two key activities. I would also like on the card commercial cleaning at Facilities maintenance.

```html
<!DOCTYPE html>
<html lang="en">
<head>
<meta charset="utf-8">
<title>Brook Estate Group – Business Card</title>
<link rel="stylesheet" href="https://fonts.googleapis.com/css2?family=Arimo:wght@400;700&display=swap">
<style>
  :root {
    --backdrop: #2a2b2d;
    --brand-blue: #1a72c0;
    --deep-blue: #1456a6;
    --ink-dark: #2b2b2b;
    --paper: #ffffff;
  }
  * { margin: 0; padding: 0; box-sizing: border-box; }
  html, body { width: 1200px; height: 874px; overflow: hidden; }
  body {
    background: var(--backdrop);
    font-family: "Arimo", Arial, sans-serif;
    display: flex; flex-direction: column; align-items: center; justify-content: center;
    gap: 40px;
  }
  .card {
    position: relative;
    width: 560px; height: 320px;
    border-radius: 22px;
    overflow: hidden;
    box-shadow: 0 14px 30px rgba(0,0,0,.45);
  }
  .card-front { background: var(--brand-blue); color: var(--paper); }
  .brand {
    display: flex; align-items: center; gap: 10px;
    font-weight: 700; letter-spacing: .5px;
  }
  .brand-dot { width: 16px; height: 16px; border-radius: 50%; background: currentColor; }
  .card-front .brand {
    position: absolute; left: 0; right: 0; top: 118px;
    justify-content: center; font-size: 38px;
  }
  .tagline {
    position: absolute; left: 0; right: 0; bottom: 42px;
    text-align: center; font-size: 16px; letter-spacing: .3px;
  }
  .tagline .divider { margin: 0 10px; }

  .card-back { background: var(--paper); }
  .card-back .swoosh { position: absolute; inset: 0; }
  .card-back .brand {
    position: absolute; left: 34px; top: 50px;
    font-size: 30px; color: var(--deep-blue);
  }
  .holder {
    position: absolute; right: 64px; top: 172px;
    text-align: right; color: var(--paper);
  }
  .holder-name { font-size: 26px; font-weight: 700; line-height: 30px; }
  .holder-title { font-size: 15px; line-height: 18px; }
  .contact-list {
    position: absolute; right: 40px; bottom: 20px;
    list-style: none; color: var(--paper); font-size: 15px; text-align: right;
  }
  .contact-list li { display: flex; align-items: center; justify-content: flex-end; gap: 10px; line-height: 22px; }
  .contact-list svg { width: 14px; height: 14px; fill: var(--paper); }
</style>
</head>
<body>
  <section class="card card-front">
    <div class="brand"><span class="brand-dot"></span>Brook Estate Group</div>
    <p class="tagline">Commercial Cleaning<span class="divider">|</span>Facilities Maintenance</p>
  </section>

  <section class="card card-back">
    <svg class="swoosh" viewBox="0 0 560 320" preserveAspectRatio="none" aria-hidden="true">
      <path d="M0,120 C20,172 120,180 220,173 C360,162 480,124 560,88 L560,320 L0,320 Z" fill="var(--ink-dark)"/>
      <path d="M0,136 C25,184 120,190 220,184 C360,173 480,128 560,90 L560,320 L0,320 Z" fill="var(--brand-blue)"/>
    </svg>
    <div class="brand"><span class="brand-dot"></span>Brook Estate Group</div>
    <div class="holder">
      <p class="holder-name">Daniel Hart</p>
      <p class="holder-title">President</p>
    </div>
    <ul class="contact-list">
      <li>0400 555 019
        <svg viewBox="0 0 24 24"><path d="M6.6 10.8a15 15 0 0 0 6.6 6.6l2.2-2.2a1 1 0 0 1 1-.25 11.4 11.4 0 0 0 3.6.6 1 1 0 0 1 1 1V20a1 1 0 0 1-1 1A17 17 0 0 1 3 4a1 1 0 0 1 1-1h3.5a1 1 0 0 1 1 1c0 1.25.2 2.450.6 3.6a1 1 0 0 1-.25 1z"/></svg>
      </li>
      <li>info@brookestate.com.au
        <svg viewBox="0 0 24 24"><path d="M2 5h20v14H2z M2 5l10 8 10-8" fill="none" stroke="#fff" stroke-width="2"/></svg>
      </li>
      <li>www.brookestate.com.au
        <svg viewBox="0 0 24 24"><circle cx="12" cy="12" r="10"/><path d="M2 12h20M12 2c3 3 3 17 0 20M12 2c-3 3-3 17 0 20" stroke="#1a72c0" stroke-width="1.5" fill="none"/></svg>
      </li>
    </ul>
  </section>
</body>
</html>
```